Simple graphic for a book or slide presentation

We are looking for a style that suits the style of our book. It's title is Harbor. Keeping a calm course through stormy seas. There will be more line drawing/graphics in the book but how you design this image will create the style for all the other simple graphics in the book (once we decide what they are). So this one design will lead to a few more to match the style of this one. We'd like the shape of the overall graphic (i.e the arrows and words/bubbles) to be circular (not a rounded square as appears in the sample attached). Perhaps the words don't need to be in ovals or bound by anything at all; perhaps they do - let's see what you see. We'd like you to choose a font or offer many different fonts you think will capture the practical yet unconventional tone of the book. The book is teaching that managing risks in life is a life-skill that can be learned. The section of the book where this graphic will be placed is called "the power of language" - basically we are saying that thoughts, words and actions create our culture and our destiny. This insight comes from Torvel Pelloru's famous quote:
Carefully watch your thoughts, for they become your words.
Manage and watch your words, for they will become your actions.
Consider and judge your actions, for they have become your habits.
Acknowledge and watch your habits, for they shall become your values.
Understand and embrace your values, for they become your destiny.

Please change the text in the middle of the graphic to say: The Human Culture Cycle

```html
<!DOCTYPE html>
<html lang="en">
<head>
<meta charset="utf-8">
<title>The Human Culture Cycle</title>
<link rel="stylesheet" href="https://fonts.googleapis.com/css2?family=Quicksand:wght@300;400&display=swap">
<style>
  :root {
    --paper: #ffffff;
    --arrow: #b8946a;
    --thoughts: #2e8a7a;
    --words: #3e2830;
    --actions: #2e4a52;
    --habits: #615d5b;
    --values: #55162a;
    --culture: #3d7a94;
    --core: #a36464;
    --core-text: #a05e5e;
  }
  html, body {
    margin: 0;
    padding: 0;
    width: 1200px;
    height: 855px;
    overflow: hidden;
    background: var(--paper);
  }
  .cycle {
    display: block;
    width: 1200px;
    height: 855px;
  }
  .stage-label {
    font-family: "Quicksand", sans-serif;
    font-weight: 300;
    font-size: 57px;
    text-anchor: middle;
  }
  .core-label {
    font-family: "Quicksand", sans-serif;
    font-weight: 300;
    font-size: 58px;
    text-anchor: middle;
    fill: var(--core-text);
  }
  .flow-arrow {
    fill: none;
    stroke: var(--arrow);
    stroke-width: 3.5;
    stroke-linecap: round;
  }
  .underline-curve {
    fill: none;
    stroke-width: 2;
    stroke-linecap: round;
  }
  .stage-thoughts { --tone: var(--thoughts); }
  .stage-words    { --tone: var(--words); }
  .stage-actions  { --tone: var(--actions); }
  .stage-habits   { --tone: var(--habits); }
  .stage-values   { --tone: var(--values); }
  .stage-culture  { --tone: var(--culture); }
  .stage .ring { stroke: var(--tone); }
  .stage .stage-label { fill: var(--tone); }
  .stage .underline-curve { stroke: var(--tone); }
  .ring { fill: url(#bubble-fill); stroke-width: 22; }
  .core-ring { fill: url(#bubble-fill); stroke: var(--core); stroke-width: 28; }
</style>
</head>
<body>
<svg class="cycle" viewBox="0 0 1754 1250" xmlns="http://www.w3.org/2000/svg" role="img" aria-label="The Human Culture Cycle: Thoughts, Words, Actions, Habits, Values, Culture">
  <defs>
    <radialGradient id="bubble-fill" cx="0.5" cy="0.62" r="0.62">
      <stop offset="0" stop-color="#ffffff"/>
      <stop offset="0.6" stop-color="#f4f4f6"/>
      <stop offset="0.88" stop-color="#c9c9cd"/>
      <stop offset="1" stop-color="#8e8e94"/>
    </radialGradient>
    <marker id="chevron" viewBox="0 0 20 20" refX="16" refY="10" markerWidth="14" markerHeight="14" markerUnits="userSpaceOnUse" orient="auto">
      <path d="M2 2 L16 10 L2 18" fill="none" stroke="#b8946a" stroke-width="2" stroke-linecap="round"/>
    </marker>
  </defs>

  <g class="flow">
    <path class="flow-arrow" d="M1030 245 Q1090 265 1128 303" marker-end="url(#chevron)"/>
    <path class="flow-arrow" d="M1282 590 Q1290 630 1286 672" marker-end="url(#chevron)"/>
    <path class="flow-arrow" d="M1130 955 Q1090 988 1040 1010" marker-end="url(#chevron)"/>
    <path class="flow-arrow" d="M716 1015 Q665 995 618 960" marker-end="url(#chevron)"/>
    <path class="flow-arrow" d="M458 672 Q450 625 456 578" marker-end="url(#chevron)"/>
    <path class="flow-arrow" d="M620 298 Q660 268 712 243" marker-end="url(#chevron)"/>
  </g>

  <g class="stage stage-thoughts">
    <circle class="ring" cx="870" cy="217" r="150"/>
    <text class="stage-label" x="870" y="235">Thoughts</text>
    <path class="underline-curve" d="M790 285 Q880 315 975 263"/>
  </g>
  <g class="stage stage-words">
    <circle class="ring" cx="1226" cy="432" r="150"/>
    <text class="stage-label" x="1226" y="450">Words</text>
    <path class="underline-curve" d="M1140 502 Q1230 532 1330 480"/>
  </g>
  <g class="stage stage-actions">
    <circle class="ring" cx="1226" cy="823" r="150"/>
    <text class="stage-label" x="1226" y="843">Actions</text>
    <path class="underline-curve" d="M1140 893 Q1230 923 1330 871"/>
  </g>
  <g class="stage stage-habits">
    <circle class="ring" cx="877" cy="1032" r="150"/>
    <text class="stage-label" x="877" y="1050">Habits</text>
    <path class="underline-curve" d="M790 1100 Q880 1130 982 1080"/>
  </g>
  <g class="stage stage-values">
    <circle class="ring" cx="528" cy="820" r="150"/>
    <text class="stage-label" x="528" y="838">Values</text>
    <path class="underline-curve" d="M440 890 Q530 920 632 868"/>
  </g>
  <g class="stage stage-culture">
    <circle class="ring" cx="528" cy="432" r="150"/>
    <text class="stage-label" x="528" y="450">Culture</text>
    <path class="underline-curve" d="M440 502 Q530 532 632 480"/>
  </g>

  <g class="core">
    <circle class="core-ring" cx="870" cy="630" r="190"/>
    <text class="core-label" x="870" y="540">The</text>
    <text class="core-label" x="870" y="610">Human</text>
    <text class="core-label" x="870" y="680">Culture</text>
    <text class="core-label" x="870" y="750">Cycle</text>
  </g>
</svg>
</body>
</html>
```